Harbor Crestline (Business Card Design)

Need business cards designed. Something modern, chic, and sleek. Mabye the back of the card should be the navy blue that is in the logo and then just the logo on the back.

Target Market(s)

Those in the hotel, office, and renovation industry

Contact Information for Business Card

1. Logo 2. Tomasz Ferreiro 3. CEO/Founder 4. Phone: (833) HarbCre / (833) 427-2273 5. Email: tomasz@theharborcrestline.com 6. Website: www.theharborcrestline.com

Font styles to use
Other font styles liked:
• Look at the logo font and base the font for everything else off of that.

Colors
0054AA
0677BA
7BADD7
CADEEF
E8F1F8

Requirements
Must have
• Colors that are associated in the logo
Nice to have
• Sleek modern clean and chic design.

```html
<!DOCTYPE html>
<html lang="en">
<head>
<meta charset="utf-8">
<title>Harbor Crestline — Business Card</title>
<link href="https://fonts.googleapis.com/css2?family=Montserrat:wght@400;500;700&display=swap" rel="stylesheet">
<style>
  :root {
    --navy: #0b1a47;
    --gold: #c9a043;
    --ink: #1f2433;
    --rule: #c9ccd4;
    --paper: #ffffff;
    --backdrop: #e9eaed;
  }
  * { box-sizing: border-box; margin: 0; padding: 0; }
  html, body { width: 1200px; height: 1200px; overflow: hidden; }
  body {
    background: var(--backdrop);
    font-family: "Montserrat", sans-serif;
    display: flex;
    flex-direction: column;
    align-items: center;
    justify-content: center;
    gap: 60px;
  }
  .card {
    position: relative;
    width: 860px;
    height: 491px;
    border-radius: 34px;
    overflow: hidden;
    box-shadow: 0 6px 18px rgba(0,0,0,0.12);
  }
  .card--front { background: var(--paper); }
  .card--back { background: var(--navy); display: flex; align-items: center; justify-content: center; }

  .brand { display: flex; align-items: center; gap: 14px; }
  .brand__square { width: 16px; height: 16px; background: var(--gold); flex: none; }
  .brand__name {
    font-weight: 500;
    letter-spacing: 0.18em;
    text-transform: uppercase;
    white-space: nowrap;
  }
  .card--front .brand {
    position: absolute; left: 0; right: 0; top: 118px; justify-content: center;
  }
  .card--front .brand__name { color: var(--navy); font-size: 34px; }
  .card--back .brand__name { color: var(--paper); font-size: 48px; }
  .card--back .brand__square { width: 22px; height: 22px; }

  .holder { position: absolute; left: 56px; bottom: 84px; }
  .holder__name {
    color: var(--navy); font-weight: 700; font-size: 28px; letter-spacing: 0.01em; text-transform: uppercase;
  }
  .holder__role { color: var(--ink); font-size: 18px; font-weight: 400; text-transform: uppercase; margin-top: 2px; }

  .divider { position: absolute; left: 428px; top: 262px; width: 1px; height: 118px; background: var(--rule); }

  .contact { position: absolute; left: 462px; top: 258px; list-style: none; }
  .contact__item {
    display: flex; align-items: center; gap: 12px;
    color: var(--ink); font-size: 17px; font-weight: 400; line-height: 1; margin-bottom: 14px;
  }
  .contact__icon { width: 20px; height: 20px; flex: none; fill: none; stroke: var(--ink); stroke-width: 1.8; }
  .contact__icon--solid { fill: var(--ink); stroke: none; }

  .band { position: absolute; bottom: 0; }
  .band--gold { left: 0; width: 548px; height: 30px; background: var(--gold); }
  .band--navy { left: 558px; right: 0; height: 42px; background: var(--navy); }
</style>
</head>
<body>

<section class="card card--front" aria-label="Business card front">
  <div class="brand">
    <span class="brand__square"></span>
    <span class="brand__name">Harbor Crestline</span>
  </div>

  <div class="divider"></div>

  <ul class="contact">
    <li class="contact__item">
      <svg class="contact__icon contact__icon--solid" viewBox="0 0 24 24" aria-hidden="true"><path d="M6.6 10.8a15 15 0 0 0 6.6 6.6l2.2-2.2a1 1 0 0 1 1-.25 11.4 11.4 0 0 0 3.6.57 1 1 0 0 1 1 1V20a1 1 0 0 1-1 1A17 17 0 0 1 3 4a1 1 0 0 1 1-1h3.5a1 1 0 0 1 1 1c0 1.25.2 2.45.57 3.57a1 1 0 0 1-.25 1z"/></svg>
      (833) HarbCre | (833) 427-2273
    </li>
    <li class="contact__item">
      <svg class="contact__icon" viewBox="0 0 24 24" aria-hidden="true"><rect x="3" y="5.5" width="18" height="13"/><path d="M3 5.5l9 7 9-7M3 18.5l7-6M21 18.5l-7-6"/></svg>
      tomasz@theharborcrestline.com
    </li>
    <li class="contact__item">
      <svg class="contact__icon" viewBox="0 0 24 24" aria-hidden="true"><circle cx="12" cy="12" r="9"/><ellipse cx="12" cy="12" rx="4" ry="9"/><path d="M3 12h18M4.5 7.5h15M4.5 16.5h15"/></svg>
      www.theharborcrestline.com
    </li>
  </ul>

  <div class="holder">
    <p class="holder__name">Tomasz Ferreiro</p>
    <p class="holder__role">CEO | Founder</p>
  </div>

  <div class="band band--gold"></div>
  <div class="band band--navy"></div>
</section>

<section class="card card--back" aria-label="Business card back">
  <div class="brand">
    <span class="brand__square"></span>
    <span class="brand__name">Harbor Crestline</span>
  </div>
</section>

</body>
</html>
```